Ink & Toner Sales Flyer

2 Sided.
Ink & Toner Flyer
Front:
Header:
Are you one of the millions who have often complained about the high prices of ink and toner replacement cartridges?
Sub Header:
Well, now you will be able to take advantage of significant discounted pricing on all major brand replacement products through Korvel Supply.
Tagline: High Quality ink and toner at the lowest prices in the market today!

You can view our line of ink & toner and pharmacy vial products on www.korvelsupply.example.

ORDER ONLINE korvelsupply.example
ORDER BY PHONE 877-414-2596
ORDER BY FAX 866-305-4182
Backside:
Highest Quality Standards Utilized and Save Up to 70% off Retail
Did you know we manufacture brand new parts and build to the highest performance and quality standards (ISO-9001). We are a direct Manufacturer.
We replace the important mechanisms with brand new components to ensure that quality and performance is up to our standards, and yours. This is not a “Drill and Fill’ that you will find in the market.
We have been producing quality products for over 30 years. We have focused on businesses that need their products at peak performance for their business.

Wide Selection for Tavrin, Quolby, ZR, Bendrook and Felquist are excellent choices.
High Print Quality, Page Yield and Longevity.

Product Guarantee
We are confident in our products’ performance and yield; we offer a 100% product replacement guarantee for 60 days from the date of purchase.
Pricing Guarantee
In the unlikely event you find a comparable product at a lower cost, we guarantee to lower our price to beat that price and reward you with a 10% discount on your next order for bringing it to our attention.
Printer Warranty
Using our Compatible Remanufactured Cartridges will not void the manufacturer’s warranty.
Savings:

OEM Quality Toner
(Savings Comparison on Attachment for Prices.)

ORDER BY FAX 866-305-4182

Please call 877-414-2596 for Special Product Orders, Vials and Toner Bundle Pricing, Vial Samples & Any Other Additional Information.

Requirements
Must have
• Logo, Pricing Comparison in Any Format

```html
<!DOCTYPE html>
<html lang="en">
<head>
<meta charset="utf-8">
<title>Korvel Supply – Ink &amp; Toner Flyer</title>
<link rel="stylesheet" href="https://fonts.googleapis.com/css2?family=Space+Mono:wght@700&family=Oswald:wght@400;500&family=Jost:wght@300;400;500&display=swap">
<style>
  :root {
    --canvas: #ffffff;
    --paper-light: #f6efe2;
    --paper-mid: #eadcc4;
    --paper-edge: #cdb796;
    --ink: #2b2622;
    --ink-soft: #5a524a;
    --red: #d8281e;
    --logo-blue: #1d5fa8;
    --rule: #3a332d;
  }
  * { box-sizing: border-box; margin: 0; padding: 0; }
  html, body { width: 1200px; height: 1120px; overflow: hidden; background: var(--canvas); }
  body { font-family: "Jost", sans-serif; color: var(--ink); }

  .spread { position: relative; width: 1200px; height: 1120px; display: flex; gap: 40px; justify-content: center; align-items: center; }

  .sheet {
    width: 540px; height: 760px; position: relative; padding: 34px 36px 30px;
    background: radial-gradient(ellipse at 50% 45%, var(--paper-light) 0%, var(--paper-mid) 75%, var(--paper-edge) 100%);
    box-shadow: 0 6px 18px rgba(0,0,0,.25);
    display: flex; flex-direction: column;
  }

  /* Front */
  .front-header {
    font-family: "Space Mono", monospace; font-weight: 700; font-size: 15.5px; line-height: 1.25;
    text-transform: uppercase; color: var(--ink); letter-spacing: .2px;
  }
  .header-rule { height: 2px; background: var(--rule); margin: 10px 0 0; opacity: .8; }
  .product-visual { width: 330px; height: 170px; margin: 18px 0 0 20px; border-radius: 6px;
    background: linear-gradient(160deg, #6b6b6b 0%, #262626 55%, #111 100%); }
  .front-sub {
    font-family: "Jost", sans-serif; font-weight: 500; font-size: 15px; line-height: 1.3;
    text-transform: uppercase; text-align: center; margin: 34px 10px 0; color: var(--ink);
  }
  .tagline {
    font-family: "Oswald", sans-serif; font-weight: 400; font-size: 31px; line-height: 1.12;
    text-transform: uppercase; text-align: center; color: var(--red); margin: 26px 0 0;
  }
  .catalog-note { font-size: 15px; text-align: center; margin: 26px 10px 0; line-height: 1.35; color: var(--ink); }
  .catalog-note strong { font-weight: 500; }

  .contact-row { margin-top: auto; display: flex; align-items: flex-end; justify-content: space-between; }
  .brand { display: flex; align-items: center; gap: 8px; }
  .brand-dot { width: 16px; height: 16px; border-radius: 50%; background: var(--logo-blue); }
  .brand-name { font-family: "Jost", sans-serif; font-weight: 500; font-size: 15px; color: var(--logo-blue); }
  .order-lines { font-weight: 300; font-size: 16px; line-height: 1.3; text-transform: uppercase; color: var(--ink-soft); }
  .order-lines span { text-transform: none; }

  /* Back */
  .back { padding: 28px 30px 24px; font-size: 10.5px; line-height: 1.4; }
  .back-lead { color: var(--ink); }
  .back-lead b { font-weight: 500; }
  .back-red { font-family: "Oswald", sans-serif; font-size: 17px; color: var(--red); text-transform: uppercase; margin: 8px 0; }
  .back p + p { margin-top: 6px; }
  .guarantee b { font-weight: 500; }

  .savings-title { font-weight: 500; font-size: 11px; margin: 12px 0 4px; }
  .price-table { width: 100%; border-collapse: collapse; font-size: 11px; }
  .price-table th { text-align: left; font-weight: 500; border-bottom: 1px solid var(--rule); padding: 3px 4px; }
  .price-table td { padding: 3px 4px; border-bottom: 1px solid rgba(58,51,45,.25); color: var(--red); }
  .price-table td:first-child { color: var(--ink); }
  .table-note { font-size: 10px; color: var(--ink-soft); margin-top: 4px; }

  .back-contact { margin-top: auto; }
  .back-contact .order-lines { font-size: 13px; text-align: left; margin: 6px 0 0 0; }
  .back-foot { font-family: "Jost", sans-serif; font-weight: 500; font-size: 12.5px; text-transform: uppercase; text-align: center; margin-top: 12px; line-height: 1.3; }
</style>
</head>
<body>
<main class="spread">

  <section class="sheet front" aria-label="Flyer front">
    <h1 class="front-header">Are you one of the millions who have often complained about the high prices of ink and toner replacement cartridges?*</h1>
    <div class="header-rule"></div>
    <div class="product-visual" role="img" aria-label="Toner cartridge with ink cartridges"></div>
    <p class="front-sub">Well, now you will be able to take advantage of significant discounted pricing on all major brand replacement products through Korvel Supply.</p>
    <h2 class="tagline">High quality ink and toner<br>at the lowest prices<br>in the market today!</h2>
    <p class="catalog-note">You can view our line of ink &amp; toner and pharmacy vial products on <strong>www.korvelsupply.example</strong>.</p>
    <div class="contact-row">
      <div class="brand"><span class="brand-dot"></span><span class="brand-name">Korvel Supply</span></div>
      <div class="order-lines">
        Order online <span>korvelsupply.example</span><br>
        Order by phone 877-414-2596<br>
        Order by fax 866-305-4182
      </div>
    </div>
  </section>

  <section class="sheet back" aria-label="Flyer back">
    <p class="back-lead"><b>Highest Quality Standards Utilized and Save Up to 70% off Retail.</b> Did you know we manufacture brand new parts and build to the highest performance and quality standards (ISO-9001). We are a direct Manufacturer. We replace the important mechanisms with brand new components to ensure that quality and performance is up to our standards, and yours. This is not a “Drill and Fill” that you will find in the market. We have been producing quality products for over 30 years. We have focused on businesses that need their products at peak performance for their business.</p>
    <p>Wide Selection for Tavrin, Quolby, ZR, Bendrook and Felquist are excellent choices.</p>
    <h3 class="back-red">High print quality, page yield and longevity.</h3>
    <div class="guarantee">
      <p><b>Product Guarantee:</b> We are confident in our products’ performance and yield; we offer a <b>100% product replacement guarantee</b> for 60 days from the date of purchase.</p>
      <p><b>Pricing Guarantee:</b> In the unlikely event you find a comparable product at a lower cost, we guarantee to lower our price to beat that price and reward you with a 10% discount on your next order for bringing it to our attention.</p>
      <p><b>Printer Warranty:</b> Using our Compatible Remanufactured Cartridges will not void the manufacturer’s warranty.</p>
    </div>
    <p class="savings-title">Savings: OEM Quality Toner</p>
    <table class="price-table">
      <thead><tr><th>Item</th><th>OEM price</th><th>Korvel price</th><th>% savings</th></tr></thead>
      <tbody>
        <tr><td>Cartridge 01</td><td>$221.99</td><td>$169.99</td><td>23%</td></tr>
        <tr><td>Cartridge 02</td><td>$393.99</td><td>$203.94</td><td>48%</td></tr>
        <tr><td>Cartridge 03</td><td>$252.00</td><td>$160.00</td><td>25%</td></tr>
        <tr><td>Cartridge 04</td><td>$289.99</td><td>$239.94</td><td>17%</td></tr>
        <tr><td>Cartridge 05</td><td>$69.99</td><td>$46.00</td><td>33%</td></tr>
        <tr><td>Cartridge 06</td><td>$65.99</td><td>$37.00</td><td>44%</td></tr>
        <tr><td>Cartridge 07</td><td>$152.99</td><td>$125.99</td><td>18%</td></tr>
      </tbody>
    </table>
    <p class="table-note">(Savings Comparison on Attachment for Prices.) View our line of ink &amp; toner and vial products on www.korvelsupply.example.</p>
    <div class="back-contact">
      <div class="brand"><span class="brand-dot"></span><span class="brand-name">Korvel Supply</span></div>
      <div class="order-lines">
        Order online <span>korvelsupply.example</span><br>
        Order by phone 877-414-2596<br>
        Order by fax 866-305-4182
      </div>
      <p class="back-foot">Please call 877-414-2596 for special product orders, vials and toner bundle pricing, vial samples &amp; any other additional information.</p>
    </div>
  </section>

</main>
</body>
</html>
```